K9R Business Cards

Business Cards

Contact Information for Business Card

Company name, owner name, license #s, phone & email

Requirements
Should not have
• mailing address

```html
<!DOCTYPE html>
<html lang="en">
<head>
<meta charset="utf-8">
<title>K9R Construction – Business Cards</title>
<link href="https://fonts.googleapis.com/css2?family=Open+Sans:wght@400;600;700&family=Arimo:wght@400;700&display=swap" rel="stylesheet">
<style>
  :root {
    --page-bg: #e4e4e2;
    --brand-blue: #0a33a0;
    --accent-red: #c8161e;
    --ink: #1c1c1c;
    --card-white: #ffffff;
    --divider: #c9c9c9;
  }
  * { margin: 0; padding: 0; box-sizing: border-box; }
  html, body { width: 1200px; height: 960px; overflow: hidden; }
  body {
    background: var(--page-bg);
    font-family: "Open Sans", Arial, sans-serif;
    position: relative;
  }
  .card {
    position: absolute;
    left: 250px;
    width: 700px;
    height: 400px;
    border-radius: 26px;
    box-shadow: 0 6px 18px rgba(0,0,0,0.18);
    overflow: hidden;
  }
  .card--front { top: 50px; background: var(--brand-blue); }
  .card--back { top: 500px; background: var(--card-white); }

  .wordmark {
    position: absolute;
    font-family: "Open Sans", Arial, sans-serif;
    font-weight: 700;
    text-transform: uppercase;
    line-height: 1;
    text-align: center;
  }
  .card--front .wordmark {
    left: 0; right: 0; top: 120px;
    color: var(--card-white);
  }
  .wordmark__name { display: block; font-size: 104px; letter-spacing: 4px; }
  .wordmark__trade { display: block; font-size: 40px; letter-spacing: 3px; margin-top: 10px; }

  .card--back .wordmark {
    left: 250px; top: 52px; width: 330px;
    color: var(--brand-blue);
  }
  .card--back .wordmark__name { font-size: 68px; letter-spacing: 3px; }
  .card--back .wordmark__trade { font-size: 26px; letter-spacing: 2px; margin-top: 6px; }

  .person {
    position: absolute;
    right: 335px; top: 240px;
  }
  .person__name {
    font-family: "Arimo", Arial, sans-serif;
    font-weight: 700;
    font-size: 32px;
    color: var(--brand-blue);
    text-transform: uppercase;
    letter-spacing: 0.5px;
    white-space: nowrap;
  }
  .person__title {
    font-family: "Arimo", Arial, sans-serif;
    font-size: 20px;
    color: var(--accent-red);
    text-align: right;
    margin-top: 2px;
  }

  .divider {
    position: absolute;
    left: 385px; top: 200px;
    width: 1px; height: 130px;
    background: var(--divider);
  }

  .contact {
    position: absolute;
    left: 410px; top: 222px;
    font-family: "Arimo", Arial, sans-serif;
    font-size: 17px;
    line-height: 1.5;
    color: var(--ink);
    list-style: none;
  }
  .contact__row { display: flex; align-items: center; gap: 8px; white-space: nowrap; }
  .contact__row svg { width: 14px; height: 14px; flex: none; fill: var(--brand-blue); }
  .contact__license { margin-top: 4px; white-space: nowrap; }
</style>
</head>
<body>

  <section class="card card--front" aria-label="Business card front">
    <div class="wordmark">
      <span class="wordmark__name">K9R</span>
      <span class="wordmark__trade">Construction</span>
    </div>
  </section>

  <section class="card card--back" aria-label="Business card back">
    <div class="wordmark">
      <span class="wordmark__name">K9R</span>
      <span class="wordmark__trade">Construction</span>
    </div>

    <div class="person">
      <p class="person__name">Dale Whitford</p>
      <p class="person__title">President</p>
    </div>

    <div class="divider"></div>

    <ul class="contact">
      <li class="contact__row">
        <svg viewBox="0 0 24 24" aria-hidden="true"><path d="M6.6 10.8a15.1 15.1 0 0 0 6.6 6.6l2.2-2.2a1 1 0 0 1 1-.25 11.4 11.4 0 0 0 3.6.57 1 1 0 0 1 1 1V20a1 1 0 0 1-1 1A17 17 0 0 1 3 4a1 1 0 0 1 1-1h3.5a1 1 0 0 1 1 1c0 1.25.2 2.45.57 3.57a1 1 0 0 1-.25 1z"/></svg>
        555-014-2276
      </li>
      <li class="contact__row">
        <svg viewBox="0 0 24 24" aria-hidden="true"><path d="M2 5h20v14H2z M2 5l10 8 10-8" /></svg>
        dwhitford@k9rbuild.com
      </li>
      <li class="contact__license">MN License #BC504417</li>
    </ul>
  </section>

</body>
</html>
```